SilverLedgerOak - Double Sided Business Card

We are looking for design options or our business cards. We are a Business Solutions and HR solutions Provider - the theme is business, for this card.

Our brand colours are represented within our logo.

Details needed to be put on the front of the business card are:

Employees name: [Sample Name]
Role: [Sample Role]

Address: Suite 4 - Level 3/48 Halloran Avenue Parramatta NSW 2150
M: 0000 000 000
P: 1300 847 213
F: 1300 847 286
E: sample@silverledgeroak.com.au
www.silverledgeroak.com.au
Updates

Reason: Hello, could we please increase our deadline by 5 days. Thanking you, Tess

Target Market(s)

Business Owners, also Candidates looking for Employment

Industry/Entity Type

Business

Contact Information for Business Card

Role: [Sample Role]

M: 0000 000 000
P: 1300 847 213
F: 1300 847 286

Font styles to use
Sans Serif

Colors
3276b5
3176b5
0455a3
85abd2
cfdeed
ffffff
000000
1b1b1b
757575

Requirements
Must have
• Details needed to be put on the front of the business card are:
• Employees name: [Sample Name]
• Role: [Sample Role]
• Address: Suite 4 - Level 3/48 Halloran Avenue Parramatta NSW 2150
• M: 0000 000 000
• P: 1300 847 213
• F: 1300 847 286
• E: sample@silverledgeroak.com.au
• www.silverledgeroak.com.au
Nice to have
• Simplicity, clean and professional.

```html
<!DOCTYPE html>
<html lang="en">
<head>
<meta charset="utf-8">
<title>SilverLedgerOak Business Card</title>
<link rel="stylesheet" href="https://fonts.googleapis.com/css2?family=Montserrat:wght@300;400;700&display=swap">
<style>
  :root {
    --brand-blue: #0455a3;
    --mid-blue: #3276b5;
    --light-blue: #85abd2;
    --navy: #14305a;
    --bg: #cfdeed;
    --white: #ffffff;
    --ink: #1b1b1b;
    --grey: #757575;
  }
  * { margin: 0; padding: 0; box-sizing: border-box; }
  html, body { width: 1200px; height: 1200px; overflow: hidden; }
  body {
    background: var(--bg);
    font-family: "Montserrat", Arial, sans-serif;
    position: relative;
  }
  .card {
    position: absolute;
    left: 180px;
    width: 840px;
    height: 480px;
    background: var(--white);
    overflow: hidden;
  }
  .card--front { top: 120px; }
  .card--back { top: 637px; }
  .swoosh { position: absolute; left: 0; top: 0; width: 840px; height: 480px; }

  .brand {
    position: absolute;
    display: flex;
    align-items: center;
    gap: 12px;
    color: var(--brand-blue);
    font-weight: 700;
    white-space: nowrap;
  }
  .brand__mark { background: var(--brand-blue); display: block; }
  .card--front .brand { left: 60px; top: 258px; font-size: 28px; }
  .card--front .brand__mark { width: 22px; height: 22px; }
  .card--back .brand { left: 0; right: 0; justify-content: center; top: 250px; font-size: 38px; }
  .card--back .brand__mark { width: 28px; height: 28px; }

  .divider {
    position: absolute; left: 361px; top: 80px;
    width: 2px; height: 320px; background: var(--navy);
  }
  .person { position: absolute; left: 408px; top: 56px; }
  .person__name { color: var(--brand-blue); font-size: 32px; font-weight: 400; letter-spacing: 0.2px; line-height: 1.1; }
  .person__role { color: var(--ink); font-size: 19px; font-weight: 300; margin-top: 6px; }

  .contacts { position: absolute; left: 408px; top: 162px; list-style: none; }
  .contacts li {
    display: flex; align-items: flex-start;
    font-size: 19px; font-weight: 300; color: var(--ink);
    line-height: 27px; margin-bottom: 13px;
    white-space: nowrap;
  }
  .contacts svg { width: 20px; height: 20px; margin: 4px 18px 0 0; flex: none; fill: var(--ink); }

  .bottom-bar { position: absolute; left: 0; bottom: 0; width: 840px; height: 8px; display: flex; }
  .bottom-bar span:nth-child(1) { width: 196px; background: var(--brand-blue); }
  .bottom-bar span:nth-child(2) { width: 344px; background: var(--navy); }
  .bottom-bar span:nth-child(3) { flex: 1; background: var(--ink); }

  .back-web {
    position: absolute; left: 0; right: 0; top: 426px;
    text-align: center; font-size: 18px; font-weight: 400; color: var(--navy);
  }
</style>
</head>
<body>

<section class="card card--front">
  <svg class="swoosh" viewBox="0 0 840 480" aria-hidden="true">
    <path d="M0 0 H236 C100 10 4 110 0 240 Z" fill="#0455a3"/>
    <path d="M232 0 C106 14 10 110 0 240 L0 250 C12 120 110 14 240 0 Z" fill="#85abd2"/>
    <path d="M222 0 C100 18 10 114 0 240 L0 236 C10 106 110 4 236 0 Z" fill="#3276b5"/>
    <path d="M240 0 C116 12 16 120 0 250 L0 256 C18 126 122 16 250 0 Z" fill="#14305a"/>
  </svg>

  <div class="brand"><span class="brand__mark"></span>SilverLedgerOak</div>
  <div class="divider"></div>

  <div class="person">
    <h1 class="person__name">SAMPLE NAME</h1>
    <p class="person__role">Sample Role</p>
  </div>

  <ul class="contacts">
    <li>
      <svg viewBox="0 0 24 24"><path d="M12 2a7 7 0 0 0-7 7c0 5 7 13 7 13s7-8 7-13a7 7 0 0 0-7-7zm0 10a3 3 0 1 1 0-6 3 3 0 0 1 0 6z"/></svg>
      <span>Suite 4 - Level 3/48 Halloran Avenue<br>Brackenfield VIC 3188</span>
    </li>
    <li>
      <svg viewBox="0 0 24 24"><path d="M6.6 10.8a15 15 0 0 0 6.6 6.6l2.2-2.2a1 1 0 0 1 1-.25 11.4 11.4 0 0 0 3.6.57 1 1 0 0 1 1 1V20a1 1 0 0 1-1 1A17 17 0 0 1 3 4a1 1 0 0 1 1-1h3.5a1 1 0 0 1 1 1c0 1.25.2 2.45.57 3.57a1 1 0 0 1-.25 1z"/></svg>
      <span>0000 000 000</span>
    </li>
    <li>
      <svg viewBox="0 0 24 24"><path d="M3 4h5v17H3zM9 7h12v14H9zm2 3v3h8v-3zm0 5v2h2v-2zm3 0v2h2v-2zm3 0v2h2v-2zm-6 3v1h2v-1zm3 0v1h2v-1zm3 0v1h2v-1z"/></svg>
      <span>1300 847 213</span>
    </li>
    <li>
      <svg viewBox="0 0 24 24"><path d="M7 3h10v5H7zM4 9h16a2 2 0 0 1 2 2v6h-4v4H6v-4H2v-6a2 2 0 0 1 2-2zm4 6v4h8v-4z"/></svg>
      <span>1300 847 286</span>
    </li>
    <li>
      <svg viewBox="0 0 24 24"><path d="M2 5h20v14H2zm2 2v1l8 5 8-5V7l-8 5z"/></svg>
      <span>sample@silverledgeroak.com.au</span>
    </li>
    <li>
      <svg viewBox="0 0 24 24" fill="none" stroke="#1b1b1b" stroke-width="1.5" style="fill:none"><circle cx="12" cy="12" r="9"/><ellipse cx="12" cy="12" rx="4" ry="9"/><path d="M3 12h18M4.5 7.5h15M4.5 16.5h15"/></svg>
      <span>www.silverledgeroak.com.au</span>
    </li>
  </ul>

  <div class="bottom-bar"><span></span><span></span><span></span></div>
</section>

<section class="card card--back">
  <svg class="swoosh" viewBox="0 0 840 480" aria-hidden="true">
    <path d="M840 480 H604 C740 470 836 370 840 250 Z" fill="#0455a3"/>
    <path d="M608 480 C734 466 830 370 840 250 L840 240 C828 360 730 466 600 480 Z" fill="#85abd2"/>
    <path d="M618 480 C740 462 830 366 840 250 L840 254 C830 374 730 476 604 480 Z" fill="#3276b5"/>
    <path d="M600 480 C724 468 824 360 840 230 L840 224 C822 354 718 464 590 480 Z" fill="#14305a"/>
  </svg>

  <div class="brand"><span class="brand__mark"></span>SilverLedgerOak</div>
  <p class="back-web">www.silverledgeroak.com.au</p>
</section>

</body>
</html>
```